Book cover - Quiet Rooms, Open Doors

Book cover for Ebook (Pagelight) and wrap around print cover (Printvale) (back, front, and spine)

The book title (may slightly change by end of brief):
(MAIN TITLE) 'Quiet Rooms, Open Doors'
(SUB HEADING) 'A Week-by-Week Practical Workbook to Loosen Nervous Habits, Quieten Doubt and Build Steady Poise'
by Dr Owen Hartley

I would like a bold, stand out cover. Contemporary. I would like to avoid stereotypical images of people looking anxious or worried. I would like the design to be more uplifting and hopeful, rather than focusing on the negative aspect of anxiety, but avoiding cliched photos of people raising their hands in the air, smiling and jumping etc. The cover should appeal to both men and women.

Trim size of book cover (for PrintVale) is 5.25" x 8" back and front with a spine size of 0.477 inches

Reason: I have decided to extend the deadline by 1 more day, not because I am unhappy with the quality of the designs, but because a few designers have contacted me to explain they have had technical difficulties when submitting their files. Thanks everyone for the hard work and great designs.

Target Market(s)

Males and females (16+) who struggle with social anxiety and shyness

Industry/Entity Type

Social

Font styles to use
Serif

Requirements
Must have
• Bold cover that is modern and contemporary. For example, I like these covers:
• http://shrtlnk.example/k4Tq9Zb
• http://shrtlnk.example/m8Wv2Hn
• http://shrtlnk.example/p3Jx6Lr
• http://shrtlnk.example/t7Gd1Qe
• http://shrtlnk.example/v2Nk8Fy
• http://shrtlnk.example/w9Bh4Cs
• http://shrtlnk.example/z5Mf3Ud
Nice to have
• Open to abstract designs.
Should not have
• No stereotypical pictures of people who look anxious or worried. Avoid cliched photos of people raising their hands in the air, smiling and jumping etc.

```html
<!DOCTYPE html>
<html lang="en">
<head>
<meta charset="utf-8">
<title>Quiet Rooms, Open Doors — Front Cover</title>
<link rel="stylesheet" href="https://fonts.googleapis.com/css2?family=Oranienbaum&family=Roboto+Slab:wght@700&display=swap">
<style>
  :root {
    --page-bg: #ffffff;
    --teal: #9fc7c9;
    --sky: #bfe7ec;
    --blush: #ecdaef;
    --paper: #ffffff;
    --ink: #1a1a1a;
    --seam: rgba(0, 0, 0, 0.10);
  }
  * { margin: 0; padding: 0; box-sizing: border-box; }
  html, body {
    width: 1200px;
    height: 1057px;
    overflow: hidden;
    background: var(--page-bg);
  }
  .canvas {
    position: relative;
    width: 1200px;
    height: 1057px;
  }
  .cover {
    position: absolute;
    left: 291px;
    top: 58px;
    width: 617px;
    height: 940px;
    background: var(--paper);
    box-shadow: 0 12px 40px rgba(0, 0, 0, 0.12);
    overflow: hidden;
  }
  .band {
    position: absolute;
    top: 0;
    height: 100%;
  }
  .band svg { display: block; width: 100%; height: 100%; }
  .band--left { left: 0; width: 147px; }
  .band--right { left: 506px; width: 111px; }
  .band--left::after,
  .band--right::before {
    content: "";
    position: absolute;
    top: 0;
    width: 6px;
    height: 100%;
  }
  .band--left::after {
    right: 0;
    background: linear-gradient(to left, var(--seam), transparent);
  }
  .band--right::before {
    left: 0;
    background: linear-gradient(to right, var(--seam), transparent);
  }
  .panel {
    position: absolute;
    left: 147px;
    top: 0;
    width: 359px;
    height: 100%;
    background: var(--paper);
    text-align: center;
    color: var(--ink);
  }
  .title {
    position: absolute;
    top: 262px;
    left: 0;
    width: 100%;
    font-family: "Oranienbaum", serif;
    font-weight: 400;
    font-size: 42px;
    line-height: 1.08;
    letter-spacing: 0.5px;
    text-transform: uppercase;
  }
  .rule {
    position: absolute;
    top: 400px;
    left: 68px;
    width: 223px;
    height: 2px;
    background: var(--ink);
  }
  .subtitle {
    position: absolute;
    top: 420px;
    left: 30px;
    width: 299px;
    font-family: "Roboto Slab", serif;
    font-weight: 700;
    font-size: 14px;
    line-height: 1.75;
  }
</style>
</head>
<body>
  <main class="canvas">
    <section class="cover" aria-label="Front cover">
      <div class="band band--left" aria-hidden="true">
        <svg viewBox="0 0 147 940" preserveAspectRatio="none">
          <rect width="147" height="940" fill="var(--blush)"/>
          <polygon points="0,0 147,0 147,218" fill="var(--sky)"/>
        </svg>
      </div>

      <div class="panel">
        <h1 class="title">Quiet Rooms,<br>Open Doors</h1>
        <div class="rule"></div>
        <p class="subtitle">A Week-by-Week Practical Workbook to Loosen Nervous Habits, Quieten Doubt and Build Steady Poise</p>
      </div>

      <div class="band band--right" aria-hidden="true">
        <svg viewBox="0 0 111 940" preserveAspectRatio="none">
          <rect width="111" height="940" fill="var(--teal)"/>
          <polygon points="0,0 111,0 111,50 0,218" fill="var(--sky)"/>
          <polygon points="0,745 111,900 111,940 0,940" fill="var(--blush)"/>
        </svg>
      </div>
    </section>
  </main>
</body>
</html>
```